Information One Page for Email

I am looking for a informative attachment I can send with an introductive email for Ridgeview Cable Works. Something I can also Mail.

Ridgeview Cable Works is the leader in Rebar Post Tension Cable Placement and Post Tension Cable repair. Outside of cable placement and repair we do concrete repair, Parking Garage restoration and

Content

Post Tension Repair and Concrete Restoration
Post-tensioning is a revolutionary method in concrete construction that enhances the strength and durability of structures. However, like all construction ele-ments, post-tension cables can experience wear and damage over time. Ensuring timely and effective repair is crucial for maintaining the safety and integrity of your building.
Why Post-Tension Cable Repair is Essential
1. **Structural Integrity**: Damaged or deteriorated cables can compromise the structural integrity of your building, leading to safety hazards and potential structural failures.
2. **Extended Lifespan**: Regular maintenance and repair of post-tension cables extend the lifespan of your structure, ensuring it remains safe and function-al for years to come.
3. **Cost-Effective**: Addressing cable issues early on prevents more severe damage and costly repairs down the line.
Common Signs of Post-Tension Cable Issues
- Cracks in concrete surfaces
- Unusual noises or popping sounds
- Visible cable ends or broken strands
- Water leakage through cracks
Our Repair Process
1. **Inspection and Assessment**: Our team conducts a thorough inspection to identify the extent of the damage and determine the appropriate repair meth-ods.
2. **Cable Repair or Replacement**: Depending on the severity, we either re-pair the existing cables or replace them with new ones to restore full functional-ity.
3. **Sealing and Protection**: After repairing, we seal the affected areas to protect against moisture and future damage.
4. **Quality Assurance**: We perform rigorous quality checks to ensure the repairs meet industry standards and the structure is safe for use.
Why Choose Us
- **Expertise and Experience**: With years of experience in post-tension cable repair, our team is skilled in handling even the most complex repairs efficiently and effectively.
- **Advanced Technology**: We use the latest technology and materials to ensure durable and long-lasting repairs.
- **Customer Satisfaction**: Our commitment to quality and customer satisfaction sets us apart. We work closely with our clients to ensure their needs are met and expectations exceeded.
Contact Us
If you suspect issues with your post-tension cables or need a routine inspection, don't hesitate to contact us. Our experts are ready to provide the best solutions to keep your structures safe and secure.
Ensure the safety and longevity of your building with our professional post-tension cable repair services. Trust us to deliver quality and reliability every time.

```html
<!DOCTYPE html>
<html lang="en">
<head>
<meta charset="utf-8">
<title>Ridgeview Cable Works – Post Tension Repair</title>
<link href="https://fonts.googleapis.com/css2?family=Tinos:wght@400;700&family=Oswald:wght@400;500&display=swap" rel="stylesheet">
<style>
:root{
  --green:#126b40;
  --green-soft:#1d7f4e;
  --grey-box:#6c6c6c;
  --ink:#1b1b1b;
  --paper:#ffffff;
  --band-text:#dce8e1;
}
*{margin:0;padding:0;box-sizing:border-box}
html,body{width:848px;height:1200px;overflow:hidden;background:var(--paper)}
.sheet{position:relative;width:848px;height:1200px;font-family:"Tinos",serif;color:var(--ink)}
.abs{position:absolute}
.brand{left:40px;top:40px;font-family:"Tinos",serif;font-weight:700;color:var(--green);font-size:50px;line-height:58px;display:flex;align-items:flex-start;gap:14px}
.brand-mark{width:18px;height:18px;background:var(--green);margin-top:20px;flex:none}
.hero-photo{left:254px;top:0;width:594px;height:235px;
  background:linear-gradient(90deg,#ffffff 0%,#8fc0a5 22%,#1d7f4e 45%,#177547 62%,#9a9a96 78%,#c9c9c4 100%)}
.hero-rule{left:642px;top:235px;width:206px;height:11px;background:var(--green)}
.tab{left:0;width:30px;background:var(--green)}
.heading{left:44px;font-weight:700;color:var(--green);text-transform:uppercase;line-height:30px}
.intro{left:41px;top:329px;width:549px;font-size:16.4px;line-height:20.4px;text-align:justify}
.card-head{height:29px;background:var(--green);color:#fff;font-family:"Oswald",sans-serif;font-size:13px;line-height:29px;padding-left:8px;text-transform:uppercase;white-space:nowrap;
  clip-path:polygon(3% 0,97% 0,100% 100%,0 100%)}
.card-body{background:var(--grey-box);color:#111;font-family:"Oswald",sans-serif;font-size:11.2px;line-height:16.3px;text-transform:uppercase;text-align:justify;padding:5px 9px}
.signs{top:731px;font-size:17px;line-height:22px;list-style:none}
.signs li{display:flex;align-items:center;gap:4px}
.signs svg{flex:none}
.why-title{left:648px;top:244px;width:194px;text-align:center;color:var(--green);font-weight:700}
.why-title .big{font-size:70px;line-height:64px;display:block;letter-spacing:-1px}
.why-title .small{font-size:29px;line-height:30px;display:block}
.why-sub{left:649px;font-family:"Oswald",sans-serif;font-size:13.5px;color:var(--green);text-transform:uppercase}
.why-text{left:650px;width:184px;font-size:14.6px;line-height:18.8px;text-align:justify}
.contact-tab{left:14px;top:1029px;width:239px;height:38px;background:var(--green);color:#fff;font-weight:700;font-size:28px;line-height:40px;padding-left:16px;
  clip-path:polygon(0 0,94% 0,100% 30%,100% 100%,0 100%)}
.contact-band{left:0;top:1066px;width:848px;height:134px;background:var(--green)}
.contact-text{left:38px;top:1079px;width:790px;color:var(--band-text);font-size:17.6px;line-height:20px;text-align:justify}
</style>
</head>
<body>
<div class="sheet">
  <div class="abs hero-photo" role="img" aria-label="Photo of a multi-storey concrete building under post-tension repair, fading into green"></div>
  <div class="abs brand"><span class="brand-mark"></span><span>Ridgeview<br>Cable Works<br>LLC</span></div>
  <div class="abs hero-rule"></div>

  <div class="abs tab" style="top:261px;height:72px"></div>
  <h1 class="abs heading" style="top:263px;font-size:36px;line-height:34px">Post Tension Repair<br><span style="font-size:29px">&amp; Concrete Restoration</span></h1>
  <p class="abs intro">Post-tensioning is a revolutionary method in concrete construction that enhances the strength and durability of structures. However, like all construction ele-ments, post-tension cables can experience wear and damage over time. Ensu-ring timely and effective repair is crucial for maintaining the safety and integrity of your building.</p>

  <div class="abs tab" style="top:432px;height:66px"></div>
  <h2 class="abs heading" style="top:435px;font-size:35px">Why Post-Tension Cable<br>Repair is Essential</h2>

  <div class="abs" style="left:44px;top:516px;width:191px"><div class="card-head">1. **Structural Integrity**:</div></div>
  <div class="abs card-body" style="left:44px;top:551px;width:191px;height:89px">Damaged or deteriorated cables can compromise the structural integrity of your building, leading to safety hazards and potential structural failures.</div>
  <div class="abs" style="left:247px;top:516px;width:191px"><div class="card-head" style="padding-left:18px">2. **Extended Lifespan**:</div></div>
  <div class="abs card-body" style="left:247px;top:551px;width:191px;height:89px">Regular maintenance and repair of post-tension cables extend the lifespan of your structure, ensuring it remains safe and function-al for years to come.</div>
  <div class="abs" style="left:449px;top:516px;width:193px"><div class="card-head">3. **Cost-Effective**:</div></div>
  <div class="abs card-body" style="left:449px;top:551px;width:193px;height:89px">Addressing cable issues early on prevents more severe damage and costly repairs down the line.</div>

  <div class="abs tab" style="top:652px;height:65px"></div>
  <h2 class="abs heading" style="top:654px;font-size:35px">Common Signs of<br>Post-Tension Cable Issues</h2>

  <ul class="abs signs" style="left:37px">
    <li><svg width="20" height="20" viewBox="0 0 20 20"><rect x="2" y="4" width="14" height="14" fill="none" stroke="#126b40" stroke-width="2"/><path d="M5 10l4 5 9-13" fill="none" stroke="#126b40" stroke-width="2.4"/></svg>Cracks in concrete surfaces</li>
    <li><svg width="20" height="20" viewBox="0 0 20 20"><rect x="2" y="4" width="14" height="14" fill="none" stroke="#126b40" stroke-width="2"/><path d="M5 10l4 5 9-13" fill="none" stroke="#126b40" stroke-width="2.4"/></svg>Unusual noises or popping sounds</li>
  </ul>
  <ul class="abs signs" style="left:334px;top:733px">
    <li><svg width="20" height="20" viewBox="0 0 20 20"><rect x="2" y="4" width="14" height="14" fill="none" stroke="#126b40" stroke-width="2"/><path d="M5 10l4 5 9-13" fill="none" stroke="#126b40" stroke-width="2.4"/></svg>Visible cable ends or broken strands</li>
    <li><svg width="20" height="20" viewBox="0 0 20 20"><rect x="2" y="4" width="14" height="14" fill="none" stroke="#126b40" stroke-width="2"/><path d="M5 10l4 5 9-13" fill="none" stroke="#126b40" stroke-width="2.4"/></svg>Water leakage through cracks</li>
  </ul>

  <div class="abs tab" style="top:787px;height:66px"></div>
  <h2 class="abs heading" style="top:802px;left:40px;font-size:35px">Our Repair Process</h2>

  <div class="abs" style="left:37px;top:871px;width:191px"><div class="card-head" style="padding-left:4px;font-size:12.4px">1. **Inspection and Assessment**:</div></div>
  <div class="abs card-body" style="left:37px;top:906px;width:191px;height:88px">Our team conducts a thorough inspection to identify the extent of the damage and determine the appropriate repair meth-ods.</div>
  <div class="abs" style="left:240px;top:871px;width:191px"><div class="card-head" style="padding-left:4px;font-size:12.2px">2. **Cable Repair or Replacement**:</div></div>
  <div class="abs card-body" style="left:240px;top:906px;width:191px;height:88px">Depending on the severity, we either re-pair the existing cables or replace them with new ones to restore full functional-ity.</div>
  <div class="abs" style="left:443px;top:871px;width:191px"><div class="card-head" style="padding-left:14px;font-size:12.4px">3. **Sealing and Protection**:</div></div>
  <div class="abs card-body" style="left:443px;top:906px;width:191px;height:88px">After repairing, we seal the affected areas to protect against moisture and future damage.</div>
  <div class="abs" style="left:646px;top:871px;width:191px"><div class="card-head" style="padding-left:15px;font-size:12.4px">4. **Quality Assurance**:</div></div>
  <div class="abs card-body" style="left:646px;top:906px;width:191px;height:88px">We perform rigorous quality checks to ensure the repairs meet industry standards and the structure is safe for use.</div>

  <h2 class="abs why-title"><span class="big">WHY</span><span class="small">CHOOSE US</span></h2>
  <div class="abs why-sub" style="top:341px">- **Expertise and Experience**:</div>
  <p class="abs why-text" style="top:380px">With years of experience in post-tension cable repair, our team is skilled in handling even the most complex repairs efficiently and effec-tively.</p>
  <div class="abs why-sub" style="top:511px">- **Advanced Technology**:</div>
  <p class="abs why-text" style="top:550px">We use the latest technology and materials to ensure durable and long-lasting repairs.</p>
  <div class="abs why-sub" style="top:642px">- **Customer Satisfaction**:</div>
  <p class="abs why-text" style="top:681px">Our commitment to quality and customer satisfaction sets us apart. We work closely with our clients to ensure their needs are met and expectations exceeded.</p>

  <div class="abs contact-band"></div>
  <div class="abs contact-tab">CONTACT US</div>
  <div class="abs contact-text">
    <p>If you suspect issues with your post-tension cables or need a routine inspection, don't hesitate to contact us. Our experts are ready to provide the best solutions to keep your structures safe and secure.</p>
    <p>Ensure the safety and longevity of your building with our professional post-tension cable repair services. Trust us to deliver quality and reliability every time.</p>
  </div>
</div>
</body>
</html>
```